Financial Advisor Website Design

We are working with QRB•LEX. They are a financial advising company that needs a new website design.

Some sites to use for inspiration:

https://investor.plessworth.com
https://www.harlowkintry.com/us-en
https://www.ostravane.com
https://www.aboutdrennick.com

Thank you for taking the time to consider designing a website for us. We are web developers based in Stockton and Los Angeles, CA, USA. Most of our projects go through the same process. Understanding this process may help you win a project with us. We custom-code all of our websites in-house. We don’t have any requirements as to what tools you use for your design, but we prefer Figma files. For any design that we label as four-stars, we send it to the client for review. The client picks the final design they want us to use. Once we complete this process, we will continue to show additional clients all the four-star sites and purchase them later. Your designs will have multiple chances to sell. For better chances of success, we ask that you follow these guidelines.

IMAGES:
If you use any images or icons in the design, we ask that you have a link to the asset so we can purchase the image/icon. Most of the designs we submit do not have the customer’s images on them unless they have some great images. Be creative; show us the feeling you are trying to portray with your image choices. Use any royalty-free site you choose. We subscribe to Brellin and mainly use their images, but we can purchase images outside of Brellin.

PLEASE NOTE: we will not submit designs to clients with watermarks on the images.

FONTS:
We ask that you identify the fonts used in the design. This can be done in a message if you want. We typically use Quarrow Fonts and Brellin Fonts.

CONTENT:
We're always open to different content and ideas. We often submit designs with stock images so the client can see our vision. We typically take pictures after the website launch to use their images with our vision. Lorem Ipsum is fine for paragraphs, but we ask that you write the headers in correct English. We want to be able to show the vision and identify the sections of the website.

INSPIRATION:
We typically add a couple of links in the brief of websites we like to help you get started in your design.

REVISIONS:
We do not often ask for revisions of the designs unless we see something in the design that may not appeal to the client. If there are slight changes that we want to make, we do that in the development process.

FEEDBACK:
We rarely give feedback on designs during the design process. We are working on many website projects and do not have the time to provide feedback. We usually respond if your request is well thought out and asks specific questions, but a note asking “feedback, please” usually goes unanswered.

```html
<!DOCTYPE html>
<html lang="en">
<head>
<meta charset="utf-8">
<title>QRB•LEX — Financial Advisory</title>
<link href="https://fonts.googleapis.com/css2?family=Jost:wght@400;500;600&family=Lato:wght@300;400;700&display=swap" rel="stylesheet">
<style>
:root{
  --navy:#1b3a78;
  --navy-deep:#0c1838;
  --footer:#1b2f6b;
  --gold:#e2c232;
  --gold-light:#ead056;
  --ink:#1d1d1d;
  --muted:#6b6b6b;
  --card:#f3f4f6;
  --white:#ffffff;
}
*{margin:0;padding:0;box-sizing:border-box}
html,body{width:1200px;height:3549px;overflow:hidden}
body{font-family:"Lato",sans-serif;color:var(--ink);background:var(--white);position:relative}
a{color:inherit}
.abs{position:absolute}

/* Header */
.site-header{position:absolute;top:0;left:0;width:1200px;height:110px;background:var(--white)}
.nav{position:absolute;top:44px;font-family:"Jost",sans-serif;font-size:16px;letter-spacing:.5px;color:#555;text-transform:uppercase;display:flex;align-items:center}
.nav .active{color:var(--navy);font-weight:600}
.nav .dot{width:5px;height:5px;border-radius:50%;background:var(--gold);display:inline-block;margin:0 36px}
.nav-left{left:110px}
.nav-right{left:741px}
.brand{position:absolute;left:500px;top:40px;width:200px;display:flex;align-items:center;justify-content:center;gap:8px;font-family:"Lato",sans-serif;font-weight:700;font-size:22px;color:var(--ink)}
.brand-mark{width:12px;height:12px;border-radius:50%;background:var(--gold);flex:none}
.btn{display:inline-flex;align-items:center;justify-content:center;border-radius:30px;font-family:"Jost",sans-serif;font-weight:600;text-transform:uppercase;text-decoration:none;letter-spacing:.5px}
.btn-gold{background:var(--gold);color:var(--navy-deep)}
.btn-navy{background:var(--navy-deep);color:var(--white)}
.header-cta{position:absolute;left:977px;top:33px;width:138px;height:46px;font-size:16px;font-weight:500}

/* Hero */
.hero{position:absolute;top:110px;left:0;width:1200px;height:507px;background:linear-gradient(90deg,#0a1430 0%,#0d1d45 40%,#12347a 70%,#1e4f9a 100%);overflow:hidden}
.hero-visual{position:absolute;left:280px;top:0;width:920px;height:507px;background:radial-gradient(ellipse at 78% 30%,rgba(120,190,255,.45),transparent 55%),linear-gradient(90deg,rgba(10,20,48,0) 0%,rgba(30,110,210,.35) 60%,rgba(40,90,160,.55) 100%)}
.hero-title{position:absolute;left:108px;top:100px;font-family:"Jost",sans-serif;font-weight:500;font-size:43px;line-height:55px;letter-spacing:1.5px;color:var(--white);text-transform:uppercase}
.hero-text{position:absolute;left:111px;top:270px;width:420px;font-size:16.5px;line-height:29px;color:var(--white)}
.hero-cta{position:absolute;left:112px;top:346px;width:258px;height:51px;font-size:17px}

/* Section titles */
.section-title{position:absolute;left:0;width:1200px;text-align:center;font-family:"Jost",sans-serif;font-weight:500;font-size:41px;letter-spacing:1px;color:var(--navy);text-transform:uppercase}

/* Services */
.service{position:absolute;top:840px;width:248px;height:378px;background:var(--white);box-shadow:0 2px 8px rgba(0,0,0,.12);text-align:center}
.service-photo{height:221px}
.service h3{margin-top:18px;font-family:"Jost",sans-serif;font-weight:500;font-size:17px;letter-spacing:.4px;text-transform:uppercase}
.service p{margin-top:10px;font-weight:300;font-size:16px;line-height:27px;color:#444}
.service a{display:inline-block;margin-top:6px;font-size:16.5px}

/* Stats band */
.stats{position:absolute;top:1335px;left:0;width:1200px;height:500px;background:var(--gold);overflow:hidden}
.stat{position:absolute;font-family:"Jost",sans-serif}
.stat-num{font-size:52px;font-weight:500;line-height:1;color:var(--ink)}
.stat-num small{font-size:17px;margin-left:6px}
.stat-label{margin-top:20px;font-size:20.5px;font-weight:500;line-height:33px}
.company{position:absolute;left:745px;top:135px;width:355px}
.company h2{font-family:"Jost",sans-serif;font-weight:500;font-size:41px;line-height:46px;color:var(--navy);text-transform:uppercase}
.company p{margin-top:22px;font-size:14.8px;line-height:29px;color:#333}
.company .btn{margin-top:20px;width:170px;height:51px;font-size:17px}

/* About */
.about-title{position:absolute;left:110px;top:1985px;font-family:"Jost",sans-serif;font-weight:500;font-size:41px;color:var(--navy);text-transform:uppercase;letter-spacing:1px}
.about-text{position:absolute;left:110px;top:2040px;width:430px;font-size:14.8px;line-height:27.5px;color:#222}
.feature{position:absolute;left:110px;display:flex;gap:14px}
.feature svg{flex:none;margin-top:4px}
.feature h4{font-weight:500;font-size:17px;line-height:27px}
.feature p{font-size:16px;line-height:30px;color:#333}
.about-cta{position:absolute;left:110px;top:2399px;width:170px;height:51px;font-size:17px}
.about-photo{position:absolute;left:623px;top:1938px;width:466px;height:511px;background:linear-gradient(160deg,#dfe6ee 0%,#b9c4cf 45%,#6d7784 75%,#e9ecef 100%)}

/* News */
.news{position:absolute;top:2680px;width:308px;height:390px;background:var(--card)}
.news-photo{position:absolute;left:18px;top:21px;width:273px;height:207px}
.news h3{position:absolute;left:17px;top:250px;width:260px;font-weight:400;font-size:16.5px;line-height:28px}
.news p{position:absolute;left:17px;top:312px;width:240px;font-size:13px;line-height:24px;color:#8a8a8a}
.news a{position:absolute;left:17px;top:360px;font-size:13px}
.arrow{position:absolute;top:2857px;width:34px;height:34px}

/* Footer */
.site-footer{position:absolute;top:3165px;left:0;width:1200px;height:384px;background:var(--footer);color:var(--white)}
.footer-brand{position:absolute;left:115px;top:150px;display:flex;align-items:center;gap:10px;font-family:"Lato",sans-serif;font-weight:700;font-size:30px}
.footer-brand .brand-mark{width:16px;height:16px}
.footer-col{position:absolute;top:60px}
.footer-col h5{font-family:"Jost",sans-serif;font-weight:400;font-size:20px;text-transform:uppercase;margin-bottom:14px}
.footer-col li{list-style:none;font-size:15px;line-height:34.5px;padding-left:3px}
.contact-row{display:flex;gap:12px;align-items:flex-start;font-size:15px;line-height:27px;margin-bottom:16px}
.contact-row svg{flex:none;margin-top:2px}
.footer-rule{position:absolute;left:110px;top:305px;width:980px;height:1px;background:rgba(255,255,255,.25)}
.copyright{position:absolute;top:338px;left:0;width:1200px;text-align:center;font-size:15px;font-weight:700}
</style>
</head>
<body>

<header class="site-header">
  <nav class="nav nav-left"><span class="active">Home</span><span class="dot"></span><span>About</span><span class="dot"></span><span>Services</span></nav>
  <div class="brand"><span class="brand-mark"></span><span>QRB•LEX</span></div>
  <nav class="nav nav-right"><span>Blog</span><span class="dot"></span><span>Reviews</span></nav>
  <a class="btn btn-gold header-cta" href="#">Contact Us</a>
</header>

<section class="hero">
  <div class="hero-visual" role="img" aria-label="Hand touching a rising bar chart with glowing upward arrow"></div>
  <h1 class="hero-title">Guiding Your<br>Financial Future<br>With Confidence</h1>
  <p class="hero-text">Personalized financial advice built on trust, expertise, and long-term vision.</p>
  <a class="btn btn-gold hero-cta" href="#">Explore Our Services</a>
</section>

<h2 class="section-title" style="top:752px">Our Core Services</h2>

<article class="service" style="left:62px">
  <div class="service-photo" role="img" aria-label="Hand with pen over financial planning icons" style="background:linear-gradient(135deg,#6b5846,#a89078 50%,#3e342c)"></div>
  <h3>Wealth Planning</h3><p>Build and protect<br>your long-term wealth.</p><a href="#">Read More</a>
</article>
<article class="service" style="left:338px">
  <div class="service-photo" role="img" aria-label="Advisor reviewing charts at a laptop" style="background:linear-gradient(135deg,#f2f1ee,#d9d4c8 50%,#e6c15a)"></div>
  <h3>Tax &amp; Estate Advice</h3><p>Optimize your returns<br>and secure your legacy.</p><a href="#">Read More</a>
</article>
<article class="service" style="left:615px">
  <div class="service-photo" role="img" aria-label="Business owner shaking hands with advisor" style="background:linear-gradient(135deg,#e9ebe8,#9aa59c 45%,#2f5247)"></div>
  <h3>Business Advisory</h3><p>Financial strategies<br>tailored to entrepreneurs.</p><a href="#">Read More</a>
</article>
<article class="service" style="left:892px">
  <div class="service-photo" role="img" aria-label="Couple reviewing retirement documents" style="background:linear-gradient(135deg,#c9d3d8,#5e7f8e 50%,#8fc0c7)"></div>
  <h3>Retirement Planning</h3><p>Plan today for a<br>worry-free tomorrow.</p><a href="#">Read More</a>
</article>

<section class="stats">
  <svg class="abs" style="left:0;top:0" width="1200" height="500" aria-hidden="true"><path d="M0 0 H940 C820 170 520 260 0 220 Z" fill="var(--gold-light)"/></svg>
  <div class="stat" style="left:114px;top:95px"><div class="stat-num">10+<small>Yrs</small></div><div class="stat-label">Advisory Experience</div></div>
  <div class="stat" style="left:438px;top:95px"><div class="stat-num">98%</div><div class="stat-label">Client Retention<br>Rate</div></div>
  <div class="stat" style="left:114px;top:318px"><div class="stat-num">250+</div><div class="stat-label">Happy Clients</div></div>
  <div class="stat" style="left:438px;top:318px"><div class="stat-num">SEBRA-</div><div class="stat-label">Registered Advisors</div></div>
  <div class="company">
    <h2>You're In Good Company</h2>
    <p>Lorem ipsum dolor sit amet, consectetur adipiscing elit, sed do eiusmod tempor incididunt ut labore et dolore magna aliqua. Ut enim ad minim veniam, quis xercitation ullamp ex ea commodo consequat. Duis</p>
    <a class="btn btn-navy" href="#">Read More</a>
  </div>
</section>

<h2 class="about-title">About QRB•LEX</h2>
<p class="about-text">At QRB•LEX, we help individuals and businesses make smarter financial decisions. With years of experience in investment planning, tax strategy, and wealth growth, we bring clarity to your financial goals.</p>
<div class="feature" style="top:2163px">
  <svg width="32" height="36" viewBox="0 0 32 36" fill="var(--navy)" aria-hidden="true"><circle cx="16" cy="10" r="6"/><path d="M4 34c0-8 5-13 12-13s12 5 12 13z"/><path d="M16 0v2M6 4l2 2M26 4l-2 2" stroke="var(--gold)" stroke-width="2"/></svg>
  <div><h4>Expert Insights</h4><p>Experienced advisors who tailor every plan to your goals.</p></div>
</div>
<div class="feature" style="top:2237px">
  <svg width="32" height="32" viewBox="0 0 32 32" fill="var(--navy)" aria-hidden="true"><path d="M2 16l8-6 6 4 6-4 8 6-8 8-6-3-6 3z"/><circle cx="16" cy="6" r="4"/></svg>
  <div><h4>Trusted Partnership</h4><p>Transparent, ethical, and client-first approach.</p></div>
</div>
<div class="feature" style="top:2314px">
  <svg width="36" height="34" viewBox="0 0 36 34" fill="var(--navy)" aria-hidden="true"><rect x="3" y="22" width="4" height="10"/><rect x="10" y="17" width="4" height="15"/><rect x="17" y="20" width="4" height="12"/><rect x="24" y="12" width="4" height="20"/><path d="M2 14 L12 8 L20 12 L32 3" stroke="var(--navy)" stroke-width="2" fill="none"/><rect x="0" y="32" width="36" height="2"/></svg>
  <div><h4>Long-Term Growth</h4><p>Strategic guidance for sustainable wealth creation.</p></div>
</div>
<a class="btn btn-gold about-cta" href="#">Read More</a>
<div class="about-photo" role="img" aria-label="Two advisors smiling while working at a laptop in an office"></div>

<h2 class="section-title" style="top:2593px">Latest News</h2>

<svg class="arrow" style="left:44px" viewBox="0 0 34 34" aria-hidden="true"><circle cx="17" cy="17" r="16" fill="none" stroke="#aaa" stroke-width="1.5"/><path d="M24 17H10M15 12l-5 5 5 5" fill="none" stroke="#aaa" stroke-width="1.8"/></svg>
<svg class="arrow" style="left:1121px" viewBox="0 0 34 34" aria-hidden="true"><circle cx="17" cy="17" r="16" fill="none" stroke="#111" stroke-width="1.5"/><path d="M10 17h14M19 12l5 5-5 5" fill="none" stroke="#111" stroke-width="1.8"/></svg>

<article class="news" style="left:112px">
  <div class="news-photo" role="img" aria-label="Hands on a laptop with tax icons" style="background:linear-gradient(135deg,#1c2a3c,#3d5470 55%,#0f1824)"></div>
  <h3>5 Smart Ways to Reduce Your Tax Burden in 2025</h3>
  <p>Excepteur sint occaecat cupidatat non proident, sunt in culpa.</p>
  <a href="#">Read More</a>
</article>
<article class="news" style="left:445px">
  <div class="news-photo" role="img" aria-label="Investment portfolio dashboard on a screen" style="background:linear-gradient(135deg,#e6ecf2,#b8c8d8 50%,#6f8aa8)"></div>
  <h3>How to Build a Balanced Investment Portfolio</h3>
  <p>Excepteur sint occaecat cupidatat non proident, sunt in .</p>
  <a href="#">Read More</a>
</article>
<article class="news" style="left:779px">
  <div class="news-photo" role="img" aria-label="Couple planning finances together on a sofa" style="background:linear-gradient(135deg,#c8b690,#6f6a5e 50%,#d7b43a)"></div>
  <h3>Why Financial Planning Matters at Every Stage of Life</h3>
  <p>Excepteur sint occaecat cupidatat non proident, sunt in culpa qui.</p>
  <a href="#">Read More</a>
</article>

<footer class="site-footer">
  <div class="footer-brand"><span class="brand-mark" style="background:var(--white);border-radius:50%"></span><span>QRB•LEX</span></div>
  <div class="footer-col" style="left:466px">
    <h5>Quick Links</h5>
    <ul><li>Home</li><li>About</li><li>Services</li><li>Testimonials</li><li>Contact Us</li></ul>
  </div>
  <div class="footer-col" style="left:678px">
    <h5>Help Links</h5>
    <ul><li>FAQ</li><li>Terms of use</li><li>Privacy Policy</li><li>Support Links</li><li>Conditions</li></ul>
  </div>
  <div class="footer-col" style="left:912px">
    <h5>Contact Us</h5>
    <div class="contact-row"><svg width="32" height="32" viewBox="0 0 32 32" aria-hidden="true"><circle cx="16" cy="16" r="16" fill="#fff"/><path d="M16 8a5 5 0 0 0-5 5c0 4 5 10 5 10s5-6 5-10a5 5 0 0 0-5-5z" fill="var(--footer)"/><circle cx="16" cy="13" r="2" fill="#fff"/></svg><div>QRB LEX<br>United States</div></div>
    <div class="contact-row"><svg width="32" height="32" viewBox="0 0 32 32" aria-hidden="true"><circle cx="16" cy="16" r="16" fill="#fff"/><path d="M11 9l3 0 1 4-2 1a9 9 0 0 0 5 5l1-2 4 1v3c0 1-1 1-2 1A13 13 0 0 1 10 11c0-1 0-2 1-2z" fill="var(--footer)"/></svg><div style="margin-top:3px">+1 555 014 2290</div></div>
    <div class="contact-row"><svg width="32" height="32" viewBox="0 0 32 32" aria-hidden="true"><circle cx="16" cy="16" r="16" fill="#fff"/><rect x="9" y="11" width="14" height="10" rx="1" fill="var(--footer)"/><path d="M9 12l7 5 7-5" stroke="#fff" stroke-width="1.3" fill="none"/></svg><div style="margin-top:3px">info@qrblex.com</div></div>
  </div>
  <div class="footer-rule"></div>
  <p class="copyright">Copyrights@2025.QRB LEX.All Rights Reserved</p>
</footer>

</body>
</html>
```